Flyer für ambulanten Pflegedienst
Zielgruppe
Ambulanter Pflegedienst, Potentielle Kunden für Grund- und Behandlungspflege, nicht nur Pflegebedürftige, sondern auch Angehörige. Flyer dient zur Auslage, beispielsweise in Wartezimmern von Ärzten.
Aufgabenstellung
Ausführliches Briefing mit Aufbau und Text in der Anlage, ebenso das Bildmaterial, Fonts, Logos. Flyer in A4 Wickelfalz, bitte die Gestaltungsvorlage mit den Maßen des Druckanbieters (ebenfalls anbei) beachten. Vorerst hauptsächlich KI-generierte/Stockfotos vorhanden, Fotoshooting folgt im Juli und Bilder werden dann ggf. nochmal ersetzt um persönliche Ebene zu erzeugen. Der erste Wurf muss aber vorerst so erfolgen. Übergabe der Daten: Druckfähiges PDF, PDF mit Ebenen und AI

```html
<!DOCTYPE html>
<html lang="de">
<head>
<meta charset="utf-8">
<title>Flyer Hauskrankenpflege Lindner</title>
<link rel="stylesheet" href="https://fonts.googleapis.com/css2?family=Lexend:wght@500;600;700&family=Montserrat:wght@400;500;600;700&display=swap">
<style>
:root{
  --navy:#1b3f8f;
  --band:#23489a;
  --green:#3c8a4a;
  --green-tint:#eef4ec;
  --lavender:#e8e9f5;
  --text:#3f3f46;
  --icon:#9fb0d6;
  --stage:#5b5b5b;
  --muted:#555;
}
*{box-sizing:border-box;margin:0;padding:0}
html,body{width:1200px;height:3208px;overflow:hidden;background:#fff}
body{position:relative;font-family:"Montserrat",sans-serif;color:var(--text)}
.abs{position:absolute}
h2,h3,.head{font-family:"Lexend",sans-serif}
.brand-top{left:0;top:0;width:1200px;height:295px;background:#fff}
.brand-top .name{position:absolute;right:90px;top:118px;font-family:"Montserrat",sans-serif;font-weight:600;font-size:46px;color:var(--navy);display:flex;align-items:center;gap:18px}
.brand-top .dot{width:26px;height:26px;border-radius:50%;background:var(--navy)}
.stage{left:0;top:295px;width:1200px;height:1105px;background:var(--stage)}
.spread{position:absolute;background:#fff;border:1px solid #bbb;box-shadow:0 2px 8px rgba(0,0,0,.15);overflow:hidden}
.outside{left:113px;top:1464px;width:956px;height:677px}
.inside{left:103px;top:2206px;width:971px;height:685px}
.body{font-size:13px;line-height:16px}
.body b{font-weight:600;color:#222}
.blue-h{color:var(--navy);font-weight:700;font-size:19px;line-height:24px}
.photo{position:absolute;border-radius:10px}
.vert{position:absolute;font-family:"Lexend",sans-serif;font-weight:700;transform:rotate(-90deg);transform-origin:left top;white-space:nowrap}
.green-h{color:var(--green);font-weight:600;font-size:18px;line-height:23px}
.item-t{font-weight:600;font-size:15px;line-height:17px}
.pill{position:absolute;left:631px;width:204px;height:18px;background:var(--band);color:#fff;font-size:12px;font-weight:600;text-align:center;line-height:18px;border-radius:0 4px 4px 0}
.lbl{position:absolute;font-family:"Montserrat",sans-serif;font-weight:600;font-size:14px}
.fonts{left:130px;top:2963px;font-family:"Lexend",sans-serif;color:var(--muted)}
.fonts .t{font-weight:700;font-size:42px;line-height:56px}
.fonts .l{font-weight:500;font-size:46px;line-height:58px;color:#666}
</style>
</head>
<body>

<header class="abs brand-top">
  <div class="name"><span class="dot"></span>Hauskrankenpflege Lindner</div>
</header>

<div class="abs stage"></div>

<!-- Outside spread -->
<section class="spread outside">
  <!-- panel: Über uns -->
  <div class="abs" style="left:26px;top:42px;width:270px">
    <h2 class="blue-h">Pflege braucht Vertrauen.<br>Und Menschen,<br>die da sind.</h2>
    <p class="body" style="margin-top:6px">Gute Pflege entsteht durch <b>Aufmerksamkeit, Erfahrung</b> und <b>ein verlässliches Team.</b><br>Bei der Hauskrankenpflege Lindner arbeiten engagierte Pflegekräfte, Betreuungskräfte und Fachpersonen Hand in Hand – <b>mit Herz, Respekt und fachlicher Kompetenz.</b> Über 40 Mitarbeitende geben Tag für Tag ihr Bestes für Sie und Ihre Angehörigen.</p>
  </div>
  <div class="abs" style="left:26px;top:322px;width:270px">
    <h2 class="blue-h">Wir sind für Sie da.</h2>
    <p class="body" style="margin-top:6px">Sie möchten sich informieren oder ein persönliches Gespräch vereinbaren? Wir beraten Sie gerne – <b>unkompliziert, persönlich und unverbindlich.</b></p>
  </div>
  <p class="abs body" style="left:26px;top:503px;color:var(--navy);font-weight:500">Bürozeiten:<br>Mo., Di., Mi., Fr. 9 bis 12 Uhr<br>und Do. 15 bis 17 Uhr</p>
  <p class="abs body" style="left:26px;top:563px;color:var(--navy)"><b style="color:var(--navy)">Hauskrankenpflege Lindner</b><br><span style="color:var(--text)">Birkenweg 12 · 31199 Feldheim</span><br><b>Telefon: 0 51 99 - 48 27 0</b><br>info@lindner-pflege.de<br>www.lindner-pflege.de</p>

  <!-- panel: Hauswirtschaft -->
  <div class="abs" style="left:310px;top:0;width:321px;height:677px;background:var(--green-tint)"></div>
  <div class="photo" role="img" aria-label="Foto: lächelnde Haushaltshilfe mit Putzeimer in grünem Poloshirt" style="left:332px;top:40px;width:279px;height:195px;background:linear-gradient(135deg,#dfe7e4,#b9cfc2 55%,#5f8f63);border:1px solid #c9d9cc"></div>
  <div class="lbl" style="left:344px;top:48px;color:var(--green)">Lindner Hausdienste</div>
  <h3 class="abs green-h" style="left:335px;top:251px">Hilfe im Haushalt.<br>Entlastung im Alltag.</h3>
  <svg class="abs" style="left:330px;top:310px" width="50" height="160" viewBox="0 0 50 160" fill="#b7c9bb">
    <circle cx="18" cy="8" r="6"/><rect x="12" y="16" width="12" height="22" rx="3"/><rect x="26" y="26" width="16" height="14" rx="2"/><rect x="12" y="38" width="4" height="14"/><rect x="20" y="38" width="4" height="14"/>
    <circle cx="14" cy="108" r="7"/><circle cx="32" cy="108" r="7"/><path d="M2 132a12 12 0 0 1 24 0zM20 132a12 12 0 0 1 24 0z"/>
  </svg>
  <div class="abs" style="left:412px;top:310px;width:210px">
    <div class="item-t" style="color:var(--green)">Hilfe im Haushalt</div>
    <p class="body">Unterstützung bei alltäg&shy;lichen Aufgaben – von der <b>Grundreinigung</b> bis zur <b>Wäschepflege.</b></p>
  </div>
  <div class="abs" style="left:412px;top:410px;width:210px">
    <div class="item-t" style="color:var(--green)">Alltagsbegleitung &amp;<br>Betreuung</div>
    <p class="body">Niemand ist gern allein und <b>wir sind für Sie da</b>, wenn Sie Gesellschaft wünschen.</p>
  </div>
  <p class="abs body" style="left:412px;top:518px;color:var(--green);font-weight:500">Bürozeiten:<br>Mo., Di., Do., Fr. 8 bis 11 Uhr</p>
  <p class="abs body" style="left:412px;top:561px;color:var(--green)"><b style="color:var(--green)">Lindner Hausdienste GmbH</b><br><span style="color:var(--text)">Birkenweg 12 · 31199 Feldheim</span><br><b>Telefon: 0 51 99 - 37 61 405</b><br>info@lindner-hausdienste.de<br>www.lindner-hausdienste.de</p>
  <div class="vert" style="left:322px;top:672px;font-size:36px;color:#fff;opacity:.9">Hauswirtschaft</div>

  <!-- panel: Titel -->
  <div class="photo" role="img" aria-label="Foto: lächelnde Pflegekraft in blauem Poloshirt mit älterer Dame" style="left:631px;top:0;width:325px;height:335px;border-radius:0;background:linear-gradient(135deg,#e9e4df,#c9b4a3 45%,#3a5aa8 80%,#dcdcdc)"></div>
  <div class="lbl" style="left:735px;top:52px;color:var(--navy);background:#fff;padding:4px 10px;border-radius:14px">Lindner Pflege</div>
  <div class="abs" style="left:631px;top:335px;width:325px;height:103px;background:var(--band)"></div>
  <h1 class="abs head" style="left:686px;top:347px;color:#fff;font-weight:500;font-size:23px;line-height:27px">Weil das <b style="font-weight:700">eigene<br>Zuhause<br>Lebensqualität</b> ist.</h1>
  <h2 class="abs blue-h" style="left:686px;top:453px;font-size:20px">Ihr ambulanter Pflege-<br>dienst für die Region.</h2>
  <p class="abs body" style="left:686px;top:505px;width:260px;font-size:12.5px;line-height:15px">Seit <b>über 30 Jahren</b> begleiten wir Menschen im <b>Raum Feldheim und Auental</b> in ihrem vertrauten Zuhause.</p>
  <div class="pill" style="top:569px">Individuelle Beratung</div>
  <div class="pill" style="top:599px">Verlässliche Versorgung</div>
  <div class="pill" style="top:629px">MD-geprüfte Qualität</div>
  <svg class="abs" style="left:843px;top:563px" width="80" height="80" viewBox="0 0 80 80" fill="none" stroke="#c6cde0" stroke-width="5" stroke-linecap="round">
    <circle cx="40" cy="40" r="34"/><path d="M24 40l12 14 26-30"/>
  </svg>
</section>

<!-- Inside spread -->
<section class="spread inside">
  <div class="abs" style="left:0;top:39px;width:274px;height:56px;background:var(--navy);border-radius:0 10px 10px 0"></div>
  <h2 class="abs head" style="left:49px;top:44px;color:#fff;font-weight:600;font-size:20px;line-height:23px">Vertrauen beginnt<br>mit Zuhören.</h2>
  <p class="abs body" style="left:49px;top:107px;width:225px">Pflege bedeutet für uns mehr als Versorgung. Es geht um Menschen, ihre Gewohnheiten, ihre Wünsche und <b>das gute Gefühl, in den eigenen vier Wänden bleiben zu können.</b></p>
  <p class="abs body" style="left:49px;top:213px;width:225px">Deshalb nehmen wir uns Zeit für persönliche Gespräche und individuelle Lösungen. Gemeinsam mit unseren Kundinnen, Kunden und Angehörigen gestalten wir eine <b>Unterstützung, die zum Leben passt</b> – nicht umgekehrt.</p>
  <div class="photo" role="img" aria-label="Foto: Pflegekräfte begleiten eine ältere Dame im Freien" style="left:46px;top:372px;width:226px;height:189px;background:linear-gradient(135deg,#cfd9c6,#9fb28c 40%,#2f4f9c 75%,#e4e0da)"></div>
  <p class="abs body" style="left:55px;top:583px;width:215px;color:var(--navy);font-weight:600">Unsere Pflege orientiert sich am Befinden der Menschen – nicht am Befund.</p>
  <div class="abs head" style="left:214px;top:598px;font-size:80px;line-height:80px;color:#d4d7e2;font-weight:700">&rdquo;</div>
  <div class="vert" style="left:6px;top:665px;font-size:38px;color:#e3e6f1">Wer wir sind</div>

  <div class="abs" style="left:317px;top:0;width:654px;height:685px;background:var(--lavender);border-left:1px solid #cfd3e6"></div>
  <h2 class="abs head" style="left:336px;top:41px;color:var(--navy);font-weight:600;font-size:27px;line-height:33px">Unterstützung, die den<br>Alltag leichter macht.</h2>
  <p class="abs body" style="left:336px;top:112px;width:300px">Jeder Mensch braucht etwas anderes. Deshalb richten wir unsere Leistungen <b>individuell</b> nach <b>Ihrer persönlichen</b> Situation aus.</p>
  <div class="photo" role="img" aria-label="Foto: Pflegekraft im Gespräch mit einer älteren Dame im Sessel" style="left:676px;top:41px;width:259px;height:230px;background:linear-gradient(135deg,#e8e2da,#c8b9aa 45%,#3557a2 70%,#d9d4cc)"></div>

  <svg class="abs" style="left:380px;top:199px" width="50" height="420" viewBox="0 0 50 420" fill="var(--icon)">
    <path d="M25 38l-14-14a8 8 0 0 1 14-9 8 8 0 0 1 14 9z"/><path d="M4 34q4 14 21 16q17-2 21-16" fill="none" stroke="var(--icon)" stroke-width="3"/>
    <circle cx="25" cy="120" r="10" fill="none" stroke="var(--icon)" stroke-width="3"/><path d="M14 100v12a11 11 0 0 0 22 0v-12" fill="none" stroke="var(--icon)" stroke-width="3"/>
    <circle cx="14" cy="232" r="5"/><rect x="10" y="239" width="8" height="20" rx="2"/><circle cx="34" cy="262" r="9" fill="none" stroke="var(--icon)" stroke-width="3"/><rect x="24" y="238" width="6" height="20"/>
    <path d="M25 392l-15-15a9 9 0 0 1 15-10 9 9 0 0 1 15 10z"/>
  </svg>
  <div class="abs" style="left:434px;top:199px;width:220px">
    <div class="item-t" style="color:var(--navy)">Grundpflege</div>
    <p class="body">Unterstützung bei <b>Körperpflege, Mobilität, Ernährung</b> und allem, was <b>Sicherheit im Alltag</b> gibt.</p>
  </div>
  <div class="abs" style="left:434px;top:298px;width:220px">
    <div class="item-t" style="color:var(--navy)">Behandlungspflege</div>
    <p class="body"><b>Medizinische Versorgung</b> nach ärztlicher Verordnung – zum Beispiel <b>Wundver&shy;sorgung, Medikamen&shy;tengabe</b> oder <b>Injektionen.</b></p>
  </div>
  <div class="abs" style="left:434px;top:418px;width:220px">
    <div class="item-t" style="color:var(--navy)">Betreuung &amp;<br>Alltagsbegleitung</div>
    <p class="body">Begleitung im Alltag, stundenweise Betreuung, <b>Unterstützung bei Demenz</b> sowie Entlastung für Angehörige.</p>
  </div>
  <div class="abs" style="left:434px;top:555px;width:220px">
    <div class="item-t" style="color:var(--navy)">Verhinderungspflege</div>
    <p class="body"><b>Auszeiten</b> im Rahmen der Verhinderungspflege, denn auch <b>pflegende Angehörige</b> müssen mal durchatmen.</p>
  </div>

  <svg class="abs" style="left:666px;top:298px" width="50" height="300" viewBox="0 0 50 300" fill="var(--icon)">
    <circle cx="14" cy="12" r="7"/><path d="M2 36a12 12 0 0 1 24 0z"/><circle cx="36" cy="16" r="6"/><rect x="28" y="0" width="18" height="10" rx="3"/><rect x="6" y="36" width="40" height="4"/>
    <path d="M25 132l18 14v20H7v-20z" fill="none" stroke="var(--icon)" stroke-width="3"/><path d="M25 160l-6-6a4 4 0 0 1 6-5 4 4 0 0 1 6 5z"/>
    <circle cx="25" cy="258" r="16"/><path d="M25 266l-7-7a5 5 0 0 1 7-6 5 5 0 0 1 7 6z" fill="#fff"/>
  </svg>
  <div class="abs" style="left:720px;top:298px;width:225px">
    <div class="item-t" style="color:var(--navy)">Beratung</div>
    <p class="body">Pflegeberatung nach § 37.3 SGB XI zur <b>Sicherstellung des Pflegegeld-Bezugs.</b> Unterstützung bei Anträgen und Hilfe bei allen Fragen rund um Pflegeleistungen.</p>
  </div>
  <div class="abs" style="left:720px;top:433px;width:225px">
    <div class="item-t" style="color:var(--navy)">Hausnotruf &amp;<br>Erreichbarkeit</div>
    <p class="body"><b>Sicherheit rund um die Uhr</b> – mit einem Team, das erreichbar bleibt.</p>
  </div>
  <div class="abs" style="left:720px;top:540px;width:225px">
    <div class="item-t" style="color:var(--navy)">Palliative Versorgung</div>
    <p class="body">Als spezialisierter Anbieter ist uns die Versorgung und Begleitung zum Ende des Lebens ein <b>besonderes Herzensanliegen.</b></p>
  </div>
  <div class="vert" style="left:326px;top:672px;font-size:40px;color:#fff">Unsere Leistungen</div>
</section>

<div class="abs fonts">
  <div class="t">Verwendete Schriften:</div>
  <div class="l">Headlines - Ornitons</div>
  <div class="l">Fließtext - Montserrat</div>
</div>

</body>
</html>
```